HARD MONEY ORIGINATOR RECRUITMENT.
Looking for individuals to help us originate loans for real estate investor financing primarily used to fix up properties and resell.
HARD MONEY ORIGINATORS WANTED
No Licensing Required
Work As Independent Contractor
1% Flat Finders Fee on Each Loan
Referral Compensation for Recruiting New Originators
Immediate Payouts
Programs Offered Nationwide
Marketing Assistance and Support Available
Email mpelton@brightquaylending.com for more information or call (800) 641-2950 Ext. 24 Brightquay Lending Services, Inc. www.brightquaylending.com NMLS #318760
Industry/Entity Type
Real Estate
Look and feel
Each slider illustrates characteristics of the customer's brand and the style your logo design should communicate.

```html
<!DOCTYPE html>
<html lang="en">
<head>
<meta charset="utf-8">
<title>Hard Money Originators Wanted</title>
<link href="https://fonts.googleapis.com/css2?family=Montserrat:wght@400;500;700&display=swap" rel="stylesheet">
<style>
  :root {
    --ink: #2a2a2a;
    --gold: #a8922b;
    --blue: #15508f;
    --navy: #1b3a6b;
    --paper: #ffffff;
    --backdrop: #f2f2f2;
  }
  html, body {
    margin: 0;
    width: 1200px;
    height: 1200px;
    overflow: hidden;
    background: var(--backdrop);
  }
  .flyer {
    position: absolute;
    left: 174px;
    top: 0;
    width: 962px;
    height: 1354px;
    background: var(--paper);
    transform: scale(0.8863);
    transform-origin: top left;
    overflow: hidden;
    font-family: "Montserrat", sans-serif;
    color: var(--ink);
  }
  .flyer__shapes {
    position: absolute;
    inset: 0;
  }
  .headline {
    position: absolute;
    left: 54px;
    top: 52px;
    margin: 0;
    font-weight: 700;
    font-size: 47px;
    line-height: 57px;
    letter-spacing: 0.5px;
  }
  .headline__accent {
    display: block;
    color: var(--gold);
    font-size: 64px;
    line-height: 76px;
    margin-top: 4px;
    letter-spacing: 1px;
  }
  .contact {
    position: absolute;
    left: 62px;
    top: 330px;
    font-size: 15px;
    line-height: 22px;
    font-weight: 400;
  }
  .contact p { margin: 0 0 14px; }
  .brand {
    position: absolute;
    left: 650px;
    top: 110px;
    width: 290px;
    display: flex;
    align-items: center;
    gap: 12px;
    font-size: 20px;
    line-height: 25px;
    font-weight: 700;
    color: var(--navy);
  }
  .brand__dot {
    flex: none;
    width: 40px;
    height: 40px;
    border-radius: 50%;
    background: var(--gold);
  }
  .perks {
    position: absolute;
    left: 50px;
    top: 836px;
    margin: 0;
    padding: 0;
    list-style: none;
    font-size: 24.5px;
    line-height: 42.6px;
    font-weight: 500;
    text-transform: uppercase;
  }
  .perks li {
    position: relative;
    padding-left: 20px;
  }
  .perks li::before {
    content: "";
    position: absolute;
    left: 2px;
    top: 18px;
    width: 9px;
    height: 9px;
    border-radius: 50%;
    background: var(--ink);
  }
  .perks__wrap { display: block; padding-left: 17px; }
  .perks__hl { color: var(--gold); font-weight: 700; }
</style>
</head>
<body>
  <div class="flyer">
    <svg class="flyer__shapes" viewBox="0 0 962 1354" width="962" height="1354">
      <defs>
        <linearGradient id="workshopTone" x1="0" y1="0" x2="1" y2="1">
          <stop offset="0" stop-color="#7a6552"/>
          <stop offset="0.5" stop-color="#4f6c95"/>
          <stop offset="1" stop-color="#2e3a4c"/>
        </linearGradient>
        <linearGradient id="portraitTone" x1="0" y1="0" x2="0" y2="1">
          <stop offset="0" stop-color="#d9b98a"/>
          <stop offset="0.45" stop-color="#a86a55"/>
          <stop offset="1" stop-color="#5b3446"/>
        </linearGradient>
      </defs>
      <polygon role="img" aria-label="Photo of a builder in a hard hat using a power tool on a timber frame"
               points="480,219 962,219 962,729 132,729" fill="url(#workshopTone)"/>
      <polygon points="132,729 232,729 215,756 115,756" fill="var(--navy)"/>
      <polygon points="962,194 962,1354 372,1354 792,729 672,729" fill="var(--blue)"/>
      <polygon points="962,300 962,372 722,729 672,729" fill="var(--navy)" opacity="0.85"/>
      <polygon points="600,0 627,0 0,922 0,884" fill="var(--blue)"/>
      <polygon role="img" aria-label="Photo of a smiling contractor in a hard hat and plaid shirt"
               points="962,714 962,1354 522,1354" fill="url(#portraitTone)"/>
    </svg>

    <div class="brand">
      <span class="brand__dot"></span>
      <span class="brand__name">Brightquay Lending Services, Inc.</span>
    </div>

    <h1 class="headline">HARD<br>MONEY<br>ORIGINATORS<span class="headline__accent">WANTED</span></h1>

    <div class="contact">
      <p>mpelton@brightquaylending.com<br>www.brightquaylending.com<br>(800) 641-2950 Ext. 24<br>NMLS #318760</p>
      <p>Brightquay Lending<br>48 Meridian Avenue<br>Tempe, AZ 85281</p>
    </div>

    <ul class="perks">
      <li><span class="perks__hl">No Licensing</span> Required</li>
      <li>Work as <span class="perks__hl">Independent Contractor</span></li>
      <li>1% Flat Finders Fee on Each Loan</li>
      <li>Referral Compensation for<span class="perks__wrap">Recruiting New Originators</span></li>
      <li>Immediate Payouts</li>
      <li>Programs Offered<span class="perks__wrap">Nationwide</span></li>
      <li>Marketing Assistance and<span class="perks__wrap">Support Available</span></li>
    </ul>
  </div>
</body>
</html>
```